Product Box packaging design for CBD Candy Company

We need a complete product box design (dieline template included in zip file) for an online-based CBD Candy product. The Company, Harrowgate Sweets, will be marketing to a mature online audience through a well-established influencer, who focuses on ASMR. We will provide detailed information as to what will be needed on each side of the product box, but need help with the aesthetic aspect of the packaging. We would like to focus on soothing/calming colors and pull in an organic/ nature aspect. The company is based in Tennessee. We will provide a color palette that will mimic the colors of the website as well. Please refer to the zip-file for all specifications.

Target Market(s)

Online subsribers to an established Influencer

Industry/Entity Type

CBD candy industry

Requirements
Must have
• Please follow the dieline template for sizing. The box is 3.5"x3.5"X1.75"
Nice to have
• We want classic, calming, with a nature/rustic and simple feel if possible

```html
<!DOCTYPE html>
<html lang="en">
<head>
<meta charset="utf-8">
<title>Harrowgate Sweets – CBD Caramels Box</title>
<link href="https://fonts.googleapis.com/css2?family=Barlow+Condensed:ital,wght@0,500;0,600;0,700;1,800&family=Barlow:wght@400;500;600&display=swap" rel="stylesheet">
<style>
  :root {
    --green: #3f8a69;
    --green-deep: #347b5c;
    --white: #ffffff;
    --stage: #eef1ef;
    --display: "Barlow Condensed", "Arial Narrow", sans-serif;
    --body: "Barlow", Arial, sans-serif;
  }
  * { box-sizing: border-box; margin: 0; padding: 0; }
  html, body { width: 1200px; height: 958px; overflow: hidden; }
  body { background: var(--stage); position: relative; font-family: var(--body); }

  .panel { position: absolute; background: var(--white); overflow: hidden; }
  .panel--top   { left: 600px; top: 119px; width: 480px; height: 480px; }
  .panel--front { left: 600px; top: 599px; width: 480px; height: 240px; }
  .panel--side  { left: 120px; top: 599px; width: 480px; height: 240px; background: var(--green); }

  .band { position: absolute; inset: 0; background: var(--green); }
  .panel--top .band   { clip-path: polygon(26% 0, 72% 0, 66% 100%, 20% 100%); }
  .panel--front .band { clip-path: polygon(0 0, 48% 0, 80% 100%, 28% 100%, 0 20%); }

  .brand { position: absolute; display: flex; align-items: center; gap: 7px; white-space: nowrap;
           color: var(--white); font-family: var(--display); font-weight: 600;
           font-size: 15px; letter-spacing: 1.5px; text-transform: uppercase; }
  .brand__dot { width: 14px; height: 14px; border: 2px solid currentColor; border-radius: 50%; flex: none; }

  .title { position: absolute; color: var(--white); font-family: var(--display); white-space: nowrap;
           font-weight: 800; font-style: italic; font-size: 46px; line-height: .92; text-transform: uppercase; }
  .title__lines { position: absolute; display: flex; flex-direction: column; gap: 4px; }
  .title__lines span { display: block; height: 2px; background: var(--white); }
  .tagline { position: absolute; background: var(--white); color: var(--green); height: 22px;
             font-family: var(--display); font-weight: 700; font-size: 14px; line-height: 22px;
             text-align: center; white-space: nowrap; }

  .net { position: absolute; color: var(--green); font-family: var(--display); white-space: nowrap;
         font-weight: 600; font-size: 11px; line-height: 1.2; text-transform: uppercase; }
  .net--light { color: var(--white); text-align: center; font-size: 13px; }

  .dose { position: absolute; display: flex; align-items: center; gap: 6px; color: var(--green); white-space: nowrap; }
  .dose--stack { flex-direction: column; align-items: flex-start; gap: 6px; }
  .dose__item { border-top: 1px solid var(--green); border-bottom: 1px solid var(--green);
                padding: 3px 4px; text-align: center; }
  .dose__value { font-family: var(--display); font-weight: 700; font-size: 20px; line-height: 1; }
  .dose__label { font-family: var(--display); font-weight: 600; font-size: 6px; letter-spacing: .3px; text-transform: uppercase; }
  .badge { width: 20px; height: 20px; margin: 4px; border: 1.5px solid var(--green); transform: rotate(45deg); flex: none; }

  .hometown { position: absolute; color: var(--green); font-family: var(--display); white-space: nowrap;
              font-weight: 600; font-size: 11px; text-transform: uppercase; line-height: 1.15; }
  .hometown__row { display: flex; align-items: center; gap: 6px; margin-top: 3px; }
  .hometown__mark { width: 18px; height: 18px; border: 1.5px solid var(--green); border-radius: 50%; flex: none; }

  .side-frame { position: absolute; inset: 14px; border: 1px solid rgba(255,255,255,.25); }
  .side-deco { position: absolute; left: 235px; top: 20px; width: 210px; height: 210px;
               border: 14px solid rgba(255,255,255,.07); border-radius: 50%; }
  .warning { position: absolute; left: 30px; top: 26px; width: 200px; color: var(--white); }
  .warning h2 { font-family: var(--display); font-weight: 700; font-size: 18px; margin-bottom: 4px; }
  .warning p { font-size: 6.2px; line-height: 1.35; margin-bottom: 6px; text-align: justify; }
  .side-badge { position: absolute; right: 22px; bottom: 22px; width: 18px; height: 18px;
                border: 1.5px solid var(--white); transform: rotate(45deg); }
</style>
</head>
<body>

<section class="panel panel--top" aria-label="Top panel">
  <div class="band"></div>
  <div class="hometown" style="left:20px; top:30px;">
    From your friends in
    <div class="hometown__row"><span class="hometown__mark"></span>Nashville,<br>Tennessee</div>
  </div>

  <div class="brand" style="left:140px; top:48px;"><span class="brand__dot"></span>Harrowgate Sweets</div>

  <div class="dose dose--stack" style="left:370px; top:40px;">
    <span class="badge"></span>
    <div class="dose__item"><div class="dose__value">35 mg</div><div class="dose__label">CBD per caramel</div></div>
    <div class="dose__item"><div class="dose__value">420 mg</div><div class="dose__label">Per box</div></div>
  </div>

  <div class="title" style="left:122px; top:140px;">CBD<br>Caramels</div>
  <div class="title__lines" style="left:200px; top:152px; width:110px;"><span></span><span></span><span></span></div>
  <div class="tagline" style="left:100px; top:236px; width:250px;">Southern Artisan CBD Candies</div>
  <div class="net net--light" style="left:110px; top:272px; width:200px;">Net Wt 2.52 OZ<br>12 / Box | 72 Grams</div>
</section>

<section class="panel panel--front" aria-label="Front panel">
  <div class="band"></div>
  <div class="brand" style="left:50px; top:22px;"><span class="brand__dot"></span>Harrowgate Sweets</div>

  <div class="dose" style="left:306px; top:36px;">
    <div class="dose__item"><div class="dose__value">35 mg</div><div class="dose__label">CBD per caramel</div></div>
    <span class="badge"></span>
    <div class="dose__item"><div class="dose__value">420 mg</div><div class="dose__label">Per box</div></div>
  </div>

  <div class="title" style="left:108px; top:80px;">CBD<br>Caramels</div>
  <div class="title__lines" style="left:186px; top:92px; width:110px;"><span></span><span></span><span></span></div>
  <div class="tagline" style="left:100px; top:186px; width:240px;">Southern Artisan CBD Candies</div>

  <div class="net" style="left:14px; top:150px;">Net Wt<br>2.52 OZ<br><span style="display:block;margin-top:3px;">12 / Box<br>72 Grams</span></div>

  <div class="hometown" style="left:366px; top:150px;">
    From your friends in
    <div class="hometown__row"><span class="hometown__mark"></span>Nashville,<br>Tennessee</div>
  </div>
</section>

<section class="panel panel--side" aria-label="Warning side panel">
  <div class="side-frame"></div>
  <div class="side-deco"></div>
  <div class="warning">
    <h2>WARNING:</h2>
    <p>This product is not intended for use by any persons under the age of 21. Keep out of the reach of children. Do not consume this product if you are pregnant, at risk of becoming pregnant, or nursing. Do not operate heavy machinery while using this product. This product contains full spectrum edible hemp, which may yield a drowsy effect, please use responsibly.</p>
    <p>It is recommended to consume no more than 2 caramels per day. Please allow sufficient time between consumption of candies. Typically, one hour is recommended.</p>
    <p>This product has not been evaluated by the Food and Drug Administration (FDA) and is not intended to diagnose, treat, prevent or cure any disease. This product is Federally legal and compliant under the 2018 U.S. Farm Bill and contains less than 0.3% THC by dry weight basis.</p>
  </div>
  <span class="side-badge"></span>
</section>

</body>
</html>
```